I am looking for help designing my new business cards. I would like rounded edges and a raised logo on the back of the card. I have 2 Logos. One with a boat in it and one without. I'd like the one on the back to be the one that includes the boat and just the name on the front. I have included multiple formats of my logo. Please let me know if you need anymore.

Target Market(s)

Potential buyers and other sales brokers

Industry/Entity Type

Sales - Yacht / Boat Sales

Contact Information for Business Card

Id liike the front to include just the business name portion of the logo along with my name (Corwin Dalby), phone number (555.318.6027), website address (www.dalbymarineco.example) and not my physical address but just "Marlow Point, SC". The back should include my full logo that has the boat included. This portion I'd prefer raised amd take up the majority of the space there. Thanks!!

Colors
0054AA
0677BA
7BADD7
CADEEF
E8F1F8
0094D4
00A9DD
6FCCEA
C7EBF8
E9F6FB

Requirements
Must have
• Double sided
Nice to have
• My email address: Corwin@dalbymarineco.example The NMTG logo somewhere small on the front of the card
Should not have
• My full address, prefer only "Marlow Point, SC"

```html
<!DOCTYPE html>
<html lang="en">
<head>
<meta charset="utf-8">
<title>Dalby Marine Co — Business Card</title>
<link rel="stylesheet" href="https://fonts.googleapis.com/css2?family=Montserrat:wght@700;800&family=Mulish:wght@400;500&display=swap">
<style>
  :root {
    --navy: #1e2f63;
    --ocean: #1b87c8;
    --sky: #00a9dd;
    --white: #ffffff;
    --backdrop: #e3edf6;
    --ink: #151a24;
  }
  * { box-sizing: border-box; margin: 0; padding: 0; }
  html, body { width: 1200px; height: 1200px; overflow: hidden; }
  body { background: var(--backdrop); position: relative; font-family: "Mulish", sans-serif; }

  .card {
    position: absolute;
    left: 159px;
    width: 882px;
    height: 519px;
    background: var(--white);
    overflow: hidden;
  }
  .card--front { top: 62px; }
  .card--back { top: 616px; }
  .card__art { position: absolute; inset: 0; width: 100%; height: 100%; }

  .wordmark {
    position: absolute;
    font-family: "Montserrat", sans-serif;
    font-weight: 800;
    color: var(--navy);
    text-align: center;
    line-height: 1;
    text-transform: uppercase;
  }
  .wordmark__main { display: block; }
  .wordmark__sub { display: block; }
  .card--front .wordmark { left: 60px; width: 300px; top: 228px; }
  .card--front .wordmark__main { font-size: 62px; letter-spacing: 1px; }
  .card--front .wordmark__sub { font-size: 20px; letter-spacing: 3px; margin-top: 6px; }

  .card--back .wordmark { left: 0; width: 100%; top: 152px; }
  .card--back .wordmark__main { font-size: 92px; letter-spacing: 2px; }
  .card--back .wordmark__sub { font-size: 30px; letter-spacing: 5px; margin-top: 8px; }

  .holder {
    position: absolute;
    right: 68px;
    top: 152px;
    text-align: right;
    color: var(--ink);
  }
  .holder__name {
    font-family: "Montserrat", sans-serif;
    font-weight: 700;
    font-size: 32px;
    letter-spacing: 1.5px;
    text-transform: uppercase;
  }
  .holder__role { font-size: 19.5px; font-weight: 500; margin-top: 10px; }

  .contact {
    position: absolute;
    right: 58px;
    top: 316px;
    list-style: none;
    color: var(--white);
    font-size: 19px;
  }
  .contact__item {
    display: flex;
    align-items: center;
    justify-content: flex-end;
    gap: 14px;
    height: 33px;
  }
  .contact__icon { width: 14px; height: 14px; flex: none; }
</style>
</head>
<body>

<section class="card card--front" aria-label="Card front">
  <svg class="card__art" viewBox="0 0 706 415" preserveAspectRatio="none" aria-hidden="true">
    <rect width="706" height="415" fill="var(--ocean)"/>
    <path d="M0,0 L215,0 C300,60 340,150 330,228 C320,300 280,360 200,415 L0,415 Z" fill="var(--white)"/>
    <path d="M330,228 C400,120 560,40 706,15 L706,160 C600,235 450,262 330,228 Z" fill="var(--white)"/>
    <path d="M50,415 C190,318 480,296 610,415 Z" fill="var(--white)"/>
    <path d="M90,415 C210,338 450,318 565,415 Z" fill="var(--navy)"/>
  </svg>

  <div class="wordmark">
    <span class="wordmark__main">Dalby</span>
    <span class="wordmark__sub">Marine Co</span>
  </div>

  <div class="holder">
    <h1 class="holder__name">Corwin Dalby</h1>
    <p class="holder__role">Bookkeeping, Accounting and Taxes</p>
  </div>

  <ul class="contact">
    <li class="contact__item">555.318.6027
      <svg class="contact__icon" viewBox="0 0 16 16" aria-hidden="true"><path d="M4 1l2.5 3-1.5 1.8c.8 1.9 2.3 3.4 4.2 4.2L11 8.5 14 11l-1.5 3C7 14 2 9 2 2.5Z" fill="var(--white)"/></svg>
    </li>
    <li class="contact__item">Corwin@dalbymarineco.example
      <svg class="contact__icon" viewBox="0 0 16 16" aria-hidden="true"><rect x="1" y="3" width="14" height="10" rx="1" fill="var(--white)"/><path d="M1.5 3.5 8 9l6.5-5.5" stroke="var(--ocean)" stroke-width="1.3" fill="none"/></svg>
    </li>
    <li class="contact__item">www.dalbymarineco.example
      <svg class="contact__icon" viewBox="0 0 16 16" aria-hidden="true"><circle cx="8" cy="8" r="6.5" fill="none" stroke="var(--white)" stroke-width="1.5"/><ellipse cx="8" cy="8" rx="2.8" ry="6.5" fill="none" stroke="var(--white)" stroke-width="1.2"/><path d="M1.5 8h13" stroke="var(--white)" stroke-width="1.2"/></svg>
    </li>
    <li class="contact__item">Marlow Point, SC
      <svg class="contact__icon" viewBox="0 0 16 16" aria-hidden="true"><path d="M8 1a4.5 4.5 0 0 0-4.5 4.5C3.5 9 8 14 8 14s4.5-5 4.5-8.5A4.5 4.5 0 0 0 8 1Z" fill="var(--white)"/><circle cx="8" cy="5.5" r="1.7" fill="var(--ocean)"/></svg>
    </li>
  </ul>
</section>

<section class="card card--back" aria-label="Card back">
  <svg class="card__art" viewBox="0 0 706 415" preserveAspectRatio="none" aria-hidden="true">
    <path d="M0,312 C150,282 300,342 450,318 C560,300 650,290 706,296 L706,415 L0,415 Z" fill="var(--ocean)"/>
    <path d="M0,330 C150,302 300,362 450,340 C560,325 650,308 706,312 L706,415 L0,415 Z" fill="var(--navy)"/>
    <path d="M350,362 C470,328 600,318 680,358 C600,342 480,345 350,362 Z" fill="var(--white)"/>
  </svg>

  <div class="wordmark">
    <span class="wordmark__main">Dalby</span>
    <span class="wordmark__sub">Marine Co</span>
  </div>
</section>

</body>
</html>
```